Roofing Company Sales Rep Business Card

Business card for sales rep to canvass and hand out to property owners/managers for free roof inspections and roof replacements.

```html
<!DOCTYPE html>
<html lang="en">
<head>
<meta charset="UTF-8">
<title>Summit Crest Roofing – Sales Rep Business Card</title>
<link href="https://fonts.googleapis.com/css2?family=Montserrat:wght@400;500;600;800&display=swap" rel="stylesheet">
<style>
  :root {
    --bg: #3a3a3a;
    --card-white: #ffffff;
    --card-black: #0b0b0b;
    --red: #e31e26;
    --ink: #1a1a1a;
    --light: #ffffff;
  }
  * { margin: 0; padding: 0; box-sizing: border-box; }
  html, body { width: 1200px; height: 1200px; overflow: hidden; }
  body {
    background: var(--bg);
    font-family: "Montserrat", sans-serif;
    position: relative;
  }
  .card {
    position: absolute;
    width: 760px;
    height: 434px;
    border-radius: 34px;
    overflow: hidden;
  }
  .card-front { left: 60px; top: 130px; background: var(--card-white); }
  .card-back { left: 380px; top: 630px; background: var(--card-black); }

  .front-bands { position: absolute; inset: 0; }

  .brand {
    position: absolute;
    display: flex;
    align-items: center;
    gap: 14px;
    font-family: "Montserrat", sans-serif;
    font-weight: 800;
    text-transform: uppercase;
    letter-spacing: 1px;
    line-height: 1;
  }
  .brand-mark { width: 22px; height: 22px; background: var(--red); flex: none; }
  .brand-front { right: 50px; top: 120px; font-size: 34px; color: var(--ink); }
  .brand-back {
    left: 50%; top: 50%; transform: translate(-50%, -50%);
    font-size: 48px; color: var(--light); white-space: nowrap;
  }
  .brand-back .brand-mark { width: 30px; height: 30px; }

  .identity {
    position: absolute;
    left: 80px;
    top: 196px;
    padding-left: 16px;
    border-left: 6px solid var(--red);
  }
  .identity-name { font-size: 30px; font-weight: 500; color: var(--red); line-height: 1; }
  .identity-role { font-size: 16px; font-weight: 400; color: var(--ink); margin-top: 4px; }

  .contact-list {
    position: absolute;
    left: 100px;
    top: 280px;
    list-style: none;
  }
  .contact-item {
    display: flex;
    align-items: center;
    gap: 12px;
    font-size: 19px;
    color: var(--ink);
    margin-bottom: 8px;
  }
  .contact-icon { width: 20px; height: 20px; flex: none; }
</style>
</head>
<body>

<section class="card card-front" aria-label="Business card front">
  <svg class="front-bands" viewBox="0 0 760 434" aria-hidden="true">
    <polygon points="600,214 760,214 760,434 585,434 585,300" fill="#111"/>
    <rect x="0" y="398" width="585" height="36" fill="var(--red)"/>
    <polygon points="490,300 580,300 580,434 460,434 460,330" fill="var(--red)"/>
  </svg>

  <div class="brand brand-front"><span class="brand-mark"></span>Summit Crest Roofing</div>

  <div class="identity">
    <div class="identity-name">FULL NAME</div>
    <div class="identity-role">POSITION</div>
  </div>

  <ul class="contact-list">
    <li class="contact-item">
      <svg class="contact-icon" viewBox="0 0 24 24" aria-hidden="true"><path fill="var(--red)" d="M6.6 10.8a15.1 15.1 0 0 0 6.6 6.6l2.2-2.2c.3-.3.7-.4 1-.2 1.1.4 2.3.6 3.6.6.6 0 1 .4 1 1V20c0 .6-.4 1-1 1A17 17 0 0 1 3 4c0-.6.4-1 1-1h3.5c.6 0 1 .4 1 1 0 1.3.2 2.5.6 3.6.1.3 0 .7-.2 1z"/></svg>
      (000) 000 0000
    </li>
    <li class="contact-item">
      <svg class="contact-icon" viewBox="0 0 24 24" aria-hidden="true"><rect x="2" y="5" width="20" height="14" fill="var(--red)"/><path d="M2 5l10 8 10-8" fill="none" stroke="#fff" stroke-width="2"/></svg>
      email@company.com
    </li>
    <li class="contact-item">
      <svg class="contact-icon" viewBox="0 0 24 24" aria-hidden="true"><g fill="none" stroke="var(--red)" stroke-width="2"><circle cx="12" cy="12" r="10"/><ellipse cx="12" cy="12" rx="4" ry="10"/><path d="M2 12h20M4 7h16M4 17h16"/></g></svg>
      www.company.com
    </li>
  </ul>
</section>

<section class="card card-back" aria-label="Business card back">
  <div class="brand brand-back"><span class="brand-mark"></span>Summit Crest Roofing</div>
</section>

</body>
</html>
```